Website Design for Trading Company

Website for a trading company. No e-commerce required but dues need an AI Bot for questions, and needs to look extremely professional. Some examples of similar websites are:
selvanmilk(dot)com
brakomel(dot)com
tovirex(dot)com
pkrcream(dot)com(dot)au

Colour theme and style can be viewed in the files below.

Target Market(s)

Business to Business

Industry/Entity Type

Dairy Trading Business

Coding

Coded - Design and coding required

Number of Pages Required

5+ page

Font styles to use
Serif
Sans Serif

Colors
0054AA
0677BA
7BADD7
CADEEF
E8F1F8
00AB8E
00BBA5
67D7C9
C6EFE9
E9F9F6
59FF00
82FF00
B8FF75
E3FFCB
F4FFEA

Requirements
Nice to have
• AI Bot

```html
<!DOCTYPE html>
<html lang="en">
<head>
<meta charset="UTF-8">
<title>Verdalo Trade – Feeding the Future</title>
<link rel="stylesheet" href="https://fonts.googleapis.com/css2?family=Poppins:wght@400;500;600;700;800&display=swap">
<style>
:root{
  --navy:#0B3F86;
  --blue:#0054AA;
  --lime:#59FF00;
  --lime-2:#82FF00;
  --lime-soft:#F4FFEA;
  --lime-pale:#E3FFCB;
  --text:#2B2B2B;
  --white:#FFFFFF;
  --black:#0A0A0A;
}
*{margin:0;padding:0;box-sizing:border-box}
html,body{width:1200px;height:3751px;overflow:hidden}
body{position:relative;font-family:"Poppins",sans-serif;color:var(--text);background:var(--white)}
.abs{position:absolute}
.btn-leaf{position:absolute;display:flex;align-items:center;justify-content:center;font-weight:700;color:var(--navy);
  background:linear-gradient(90deg,var(--lime-pale) 0%,var(--lime-2) 45%,var(--lime) 100%);border-radius:30px 0 30px 0}

/* header */
.site-header{position:absolute;top:0;left:0;width:1200px;height:75px;background:var(--white)}
.brand{position:absolute;left:104px;top:10px;font-weight:800;font-size:42px;color:var(--navy);line-height:1;letter-spacing:-0.5px}
.brand-tag{position:absolute;left:127px;top:57px;font-size:9px;font-weight:600;letter-spacing:3px;color:var(--navy)}
.main-nav{position:absolute;top:27px;left:0;width:1200px;font-weight:600;font-size:16px;color:#222}
.main-nav span{position:absolute}

/* hero */
.hero{position:absolute;top:75px;left:0;width:1200px;height:609px;overflow:hidden;
  background:linear-gradient(180deg,#5C83A8 0%,#8FB0CC 28%,#C9D9E3 48%,#7C9A55 55%,#5C8A2E 72%,#4E7D26 100%)}
.hero-title{position:absolute;top:122px;width:1200px;text-align:center;color:var(--white);font-weight:800;font-size:54px;line-height:60px}
.hero-text{position:absolute;top:258px;left:190px;width:820px;text-align:center;color:var(--white);font-size:17.5px;line-height:28px}

/* about */
.about-photo{position:absolute;left:105px;top:756px;width:420px;height:420px;border-radius:50%;
  background:radial-gradient(circle at 40% 40%,#D9E6EE 0%,#9FB4C4 45%,#4E6B84 100%)}
.section-title{position:absolute;font-weight:800;color:var(--navy);letter-spacing:0.3px}
.about-text{position:absolute;left:591px;top:832px;width:498px;font-size:17px;line-height:28.2px;text-align:justify;color:#333}

/* expertise */
.expertise{position:absolute;top:1283px;left:0;width:1200px;height:727px;background:var(--lime-soft)}
.exp-card{position:absolute;top:1474px;height:412px}
.exp-photo{position:absolute;top:0;left:0;width:100%;height:212px;border-radius:50% 50% 0 0 / 26% 26% 0 0}
.exp-body{position:absolute;top:212px;left:0;width:100%;height:200px;background:var(--navy);color:var(--white);text-align:center;padding:0 8px}
.exp-body h3{margin-top:26px;font-size:14.5px;font-weight:700}
.exp-body p{margin-top:10px;font-size:18px;line-height:28.5px;white-space:nowrap}
.dots{position:absolute;top:1959px;left:585px;display:flex;gap:3px}
.dots i{width:8px;height:8px;border-radius:50%;background:#BFBFBF;display:block}

/* services */
.services-band{position:absolute;top:2010px;left:0;width:1200px;height:334px;
  background:linear-gradient(180deg,#1C4D86 0%,#244F73 55%,#2E5D5A 100%)}
.service-circle{position:absolute;top:2224px;width:213px;height:213px;border-radius:50%;background:var(--white);
  box-shadow:0 6px 16px rgba(0,0,0,.18);display:flex;align-items:center;justify-content:center}
.service-circle.is-active{background:radial-gradient(circle at 70% 70%,var(--lime-2),var(--lime) 60%,#7BE82A)}
.service-label{position:absolute;top:2466px;width:240px;text-align:center;font-size:14px;font-weight:700;color:var(--navy)}
.services-text{position:absolute;top:2523px;left:156px;width:888px;text-align:center;font-size:18px;line-height:28.5px;color:#333}

/* contact */
.contact-bg{position:absolute;top:2704px;left:0;width:1200px;height:696px;
  background:linear-gradient(180deg,var(--lime-soft) 0%,#E4EDD8 38%,#B9B99A 62%,#6F7A3D 82%,#4D5B22 100%)}
.cow-photo{position:absolute;left:0;top:2840px;width:450px;height:520px;border-radius:0 48% 38% 0;
  background:radial-gradient(circle at 40% 45%,#EDEDED 0%,#9A9A9A 45%,#2A2A2A 80%)}
.contact-card{position:absolute;left:211px;top:2793px;width:775px;height:447px;background:var(--white);border-radius:58px}
.field{position:absolute;border:1.5px solid #333;border-radius:28px;font-size:14px;color:#444;padding:0 20px;display:flex;align-items:center}
.field.is-area{align-items:flex-start;padding-top:18px}

/* footer */
.site-footer{position:absolute;top:3400px;left:0;width:1200px;height:351px;background:var(--black);border-top:6px solid var(--white)}
.footer-brand{position:absolute;left:0;top:72px;width:1200px;text-align:center;font-weight:800;font-size:56px;color:var(--blue);line-height:1}
.footer-tag{position:absolute;top:132px;left:0;width:1200px;text-align:center;font-size:11px;font-weight:600;letter-spacing:4px;color:var(--blue)}
.footer-nav{position:absolute;top:192px;left:0;width:1200px;font-weight:600;font-size:16px;color:var(--white)}
.footer-nav span{position:absolute}
.social{position:absolute;top:254px;left:0;width:1200px;display:flex;justify-content:center;gap:28px}
.social i{width:14px;height:14px;border-radius:50%;background:var(--white);display:block}
.footer-rule{position:absolute;top:292px;left:113px;width:974px;height:1px;background:#9A9A9A}
.copyright{position:absolute;top:310px;left:117px;font-size:15px;color:var(--white)}
</style>
</head>
<body>

<header class="site-header">
  <div class="brand">Verdalo</div>
  <div class="brand-tag">FEEDING THE FUTURE</div>
  <nav class="main-nav">
    <span style="left:430px">HOME</span>
    <span style="left:547px">ABOUT US</span>
    <span style="left:690px">OUR EXPERTISE</span>
    <span style="left:869px">SERVICE</span>
    <span style="left:1002px">CONTACT</span>
  </nav>
</header>

<section class="hero">
  <div class="abs" role="img" aria-label="Sunny pasture with grazing dairy cows under a blue sky" style="inset:0"></div>
  <h1 class="hero-title">WELCOME TO<br>VERDALO FEEDING THE FUTURE</h1>
  <p class="hero-text">Lorem Ipsum is simply dummy text of the printing and typesetting industry. Lorem Ipsum has been the industry's standard dummy text ever since the 1500s, when an unknown printer</p>
  <div class="btn-leaf" style="left:501px;top:352px;width:226px;height:64px;font-size:21px">GET STARTED</div>
</section>

<div class="about-photo" role="img" aria-label="Dairy bottling line filling milk bottles with a glass of milk in front"></div>
<h2 class="section-title" style="left:591px;top:765px;font-size:38px">ABOUT US</h2>
<p class="about-text">Sed ut perspiciatis unde omnis iste natus error sit voluptatem accusantium doloremque laudantium, totam rem aperiam, eaque ipsa quae ab illo inventore veritatis et quasi architecto beatae vitae dicta sunt explicabo. Nemo enim ipsam voluptatem quia voluptas sit aspernatur aut odit aut fugit, sed quia consequuntur magni dolores eos qui ratione voluptatem sequi nesciunt. Neque porro quisquam est, qui dolorem ipsum quia dolor sit amet, consectetur, adipisci velit.</p>
<div class="btn-leaf" style="left:581px;top:1124px;width:193px;height:56px;font-size:17px">READ MORE</div>

<section class="expertise"></section>
<h2 class="section-title" style="left:0;width:1200px;text-align:center;top:1386px;font-size:40px">OUR EXPERTISE</h2>

<article class="exp-card" style="left:105px;width:310px">
  <div class="exp-photo" role="img" aria-label="Milk being poured from steel dairy equipment" style="background:linear-gradient(160deg,#C9B79A,#6E5A3E 60%,#2E241A)"></div>
  <div class="exp-body"><h3>LOREM IPSUM IS SIMPLY</h3><p>Sed ut perspiciatis unde omnis<br>iste natus error sit voluptatem<br>accusantium doloremque lau-<br>dantium, totam rem aperiam</p></div>
</article>
<article class="exp-card" style="left:446px;width:309px">
  <div class="exp-photo" role="img" aria-label="Children drinking glasses of milk at a table" style="background:linear-gradient(160deg,#F2ECE3,#CDBFAE 55%,#8E8170)"></div>
  <div class="exp-body"><h3>LOREM IPSUM IS SIMPLY</h3><p>Sed ut perspiciatis unde omnis<br>iste natus error sit voluptatem<br>accusantium doloremque lau-<br>dantium, totam rem aperiam</p></div>
</article>
<article class="exp-card" style="left:780px;width:309px">
  <div class="exp-photo" role="img" aria-label="Cows grazing in a green field at sunset" style="background:linear-gradient(180deg,#5C86A8,#D9B86A 45%,#5E8A2E 75%,#3F6A1E)"></div>
  <div class="exp-body"><h3>LOREM IPSUM IS SIMPLY</h3><p>Sed ut perspiciatis unde omnis<br>iste natus error sit voluptatem<br>accusantium doloremque lau-<br>dantium, totam rem aperiam</p></div>
</article>
<div class="dots"><i></i><i></i><i></i></div>

<section class="services-band" role="img" aria-label="Close-up of cattle in a field with a blue tint"></section>
<h2 class="section-title" style="left:0;width:1200px;text-align:center;top:2112px;font-size:38px;color:var(--white)">SERVICES</h2>

<div class="service-circle is-active" style="left:127px">
  <svg width="104" height="100" viewBox="0 0 104 100" fill="none" stroke="#111" stroke-width="4">
    <rect x="6" y="28" width="30" height="66"/><path d="M6 28 L14 10 H30 L36 28"/>
    <rect x="58" y="30" width="22" height="64" rx="6"/><rect x="63" y="10" width="12" height="20"/>
    <rect x="82" y="60" width="18" height="34"/>
  </svg>
</div>
<div class="service-circle" style="left:366px">
  <svg width="80" height="112" viewBox="0 0 80 112" fill="none" stroke="#111" stroke-width="4">
    <rect x="10" y="30" width="60" height="78" rx="10"/><rect x="20" y="18" width="40" height="12"/>
    <path d="M10 62 H70"/><path d="M4 8 H30 M30 4 V12"/>
  </svg>
</div>
<div class="service-circle" style="left:606px">
  <svg width="80" height="112" viewBox="0 0 80 112" fill="none" stroke="#111" stroke-width="4">
    <path d="M6 10 H74 L62 38 H18 Z"/><path d="M40 38 V56"/>
    <path d="M16 64 H64 L58 106 H22 Z"/>
  </svg>
</div>
<div class="service-circle" style="left:845px">
  <svg width="140" height="90" viewBox="0 0 140 90" fill="none" stroke="#111" stroke-width="4">
    <rect x="6" y="16" width="90" height="40" rx="20"/>
    <path d="M100 30 H122 L134 48 V66 H100 Z"/><path d="M6 66 H100"/>
    <circle cx="30" cy="72" r="8"/><circle cx="52" cy="72" r="8"/><circle cx="116" cy="72" r="8"/>
    <text x="34" y="42" font-family="Poppins,sans-serif" font-size="15" stroke="none" fill="#111" font-weight="600">MILK</text>
  </svg>
</div>
<div class="service-label" style="left:113px">LOREM IPSUM IS SIMPLY</div>
<div class="service-label" style="left:353px">LOREM IPSUM IS SIMPLY</div>
<div class="service-label" style="left:593px">LOREM IPSUM IS SIMPLY</div>
<div class="service-label" style="left:832px">LOREM IPSUM IS SIMPLY</div>
<p class="services-text">Sed ut perspiciatis unde omnis iste natus error sit voluptatem accusantium doloremque laudantium, totam rem aperiam, eaque ipsa quae ab illo inventore veritatis et quasi architecto beatae vitae dicta sunt explicabo. Nemo enim ipsam voluptatem quia voluptas sit aspernatur aut odit aut fugit, sed quia consequuntur magni dolores eos qui ratione</p>

<section class="contact-bg" role="img" aria-label="Misty pasture with a herd of cows"></section>
<div class="cow-photo" role="img" aria-label="Black and white dairy cow looking in from the left"></div>
<div class="contact-card"></div>
<h2 class="section-title" style="left:492px;top:2834px;font-size:39px">CONTACT US</h2>
<div class="field" style="left:483px;top:2903px;width:204px;height:55px">FIRST NAME</div>
<div class="field" style="left:694px;top:2903px;width:209px;height:55px">LAST NAME</div>
<div class="field" style="left:483px;top:2969px;width:420px;height:55px">EMAIL</div>
<div class="field is-area" style="left:483px;top:3036px;width:420px;height:95px">MESSAGE</div>
<div class="btn-leaf" style="left:483px;top:3142px;width:193px;height:56px;font-size:15px;font-weight:500;color:#111">SUBMIT</div>

<footer class="site-footer">
  <div class="footer-brand">Verdalo</div>
  <div class="footer-tag">FEEDING THE FUTURE</div>
  <nav class="footer-nav">
    <span style="left:259px">HOME</span>
    <span style="left:376px">ABOUT US</span>
    <span style="left:520px">OUR EXPERTISE</span>
    <span style="left:699px">SERVICE</span>
    <span style="left:831px">CONTACT</span>
  </nav>
  <div class="social" aria-label="Social links"><i></i><i></i><i></i><i></i><i></i></div>
  <div class="footer-rule"></div>
  <div class="copyright">© 2023 verdalotrade</div>
</footer>

</body>
</html>
```